Looking for a unique designer to design new & exciting stationery for progressive professional firm

Hello! We would like to stand out, but in a good way. We want a modern unique image, something creative, but remain professional. Also portray integrity and look approachable. We want to appeal to the younger generation while not losing the respect of our more conservative older clients!

Our focus at Harbourline Partners is on guiding our clients and assisting them to 'move in the right direction'. We are a small boutique accounting firm based in Melbourne Australia.

Using our 2 distinctive colours (blue & yellow) and new logo design attached, please design a modern and professional letterhead, with compliments slip and business card for our firm.

The necessary words and logos to be included on the letterhead and card are attached, the overall design of the stationery however is up to your talent. Font to be modern, professional & progressive! I like the font style (LV docs Trebuchet MS) on my draft letterhead design attached. It looks modern, professional but approachable so something like that would be great.

For the business card, I like the attached version's REAR side of the business card but not the front side, so please come up with a design for the front that will match the letterhead design you come up with. I don't like how the company name sits tightly below the logo, they make the logo look too large in proportion to the words. Also feel free to change the rear side if you believe you have a better design :)

The colours are blue R31 G125 B165
and yellow R224 G201 B24, but please convert to CMYK equivalent.

At full sizing for the card, withcomps slip and letterhead respectively, the images need to be at least 300 dpi or higher.

Please advise if you need any other files (eg for higher resolution) or information and/or refer to our website for further input.

Thank you, with great anticipation...

Dale

Target Market(s)

Discerning (and wealthy?) clients, both business owners and personal, looking for a progressive, approachable but professional accounting firm. Need to attract and appeal to the younger generations while not losing the respect of the older more conservative generation.

Industry/Entity Type

Accounting

Font styles to use
Other font styles liked:
• Something like LV doc's Trebuchet MS - for company name. Happy for you to suggest other font for other wording.

Requirements
Must have
• My company logo, QFA logo, the wording I have included on the sample of letterhead and business card.
• The colours are blue R31 G125 B165 and yellow R224 G201 B24, but please convert to CMYK equivalent. Also use a grey for smaller wording. Refer sample letterhead attached. Note that the blue and yellow on the QFA logo are not the same as the my blue and yellow above. They will and should look different.
• Note: QFA logo must have a space around it of at least half the width of the yellow part of the logo - per my attached letter sample. The logo must be at least 15mm in width on all stationery. Also the QFA logo must have the words adjacent to it, 'Harbourline Partners Pty Ltd is a QFA practice'.
Nice to have
• Maybe curved features at bottom and/or top of letterhead instead of the rectangle coloured bars that my sample letter has.
• Good to maybe have Icons for telephone, fax email address etc.
Should not have
• No other colours except my blue, yellow and black, grey and white.
• No detailed pictures as I want to keep the design modern, minimalistic and flat.

```html
<!DOCTYPE html>
<html lang="en">
<head>
<meta charset="utf-8">
<title>Harbourline Partners — Letterhead</title>
<link rel="stylesheet" href="https://fonts.googleapis.com/css2?family=PT+Sans:wght@400;700&display=swap">
<style>
  :root {
    --brand-blue: #1f7da5;
    --brand-yellow: #e0c918;
    --ink-grey: #6f7276;
    --paper: #ffffff;
    --backdrop: #f3f3f3;
    --sheet-edge: #d9d9d9;
  }
  * { margin: 0; padding: 0; box-sizing: border-box; }
  html, body {
    width: 1200px; height: 1056px; overflow: hidden;
    background: var(--backdrop);
    font-family: "PT Sans", "Trebuchet MS", sans-serif;
  }
  .letterhead {
    position: absolute; left: 260px; top: 56px;
    width: 670px; height: 942px;
    background: var(--paper);
    border: 1px solid var(--sheet-edge);
    overflow: hidden;
  }
  .brand {
    position: absolute; left: 43px; top: 45px;
    display: flex; align-items: center; gap: 12px;
  }
  .brand-dot {
    width: 70px; height: 70px; border-radius: 50%;
    background: var(--brand-blue);
  }
  .brand-name {
    color: var(--brand-blue);
    font-weight: 700; font-size: 27px; line-height: 26px;
    text-transform: uppercase; letter-spacing: 0.2px;
  }
  .contact {
    position: absolute; right: 16px; top: 48px;
    text-align: right; color: var(--ink-grey);
    font-size: 10.5px; line-height: 12px;
  }
  .practice {
    display: flex; align-items: flex-start; justify-content: flex-end; gap: 8px;
  }
  .practice-badge {
    width: 46px; height: 20px; margin-top: 2px;
    background: var(--brand-blue);
    border-right: 14px solid var(--brand-yellow);
  }
  .contact-list { list-style: none; margin-top: 8px; }
  .contact-list li {
    display: flex; justify-content: flex-end; align-items: center; gap: 8px;
    height: 13px;
  }
  .contact-list svg { width: 9px; height: 9px; fill: var(--brand-blue); }
  .address { margin-top: 6px; margin-right: 17px; }
  .footer-rule {
    position: absolute; left: 0; right: 0; top: 846px; height: 6px;
    background: var(--brand-yellow);
  }
  .footer {
    position: absolute; left: 0; right: 0; top: 852px; bottom: 0;
    background: var(--brand-blue);
    color: #fff; text-align: center;
    font-size: 12px; line-height: 14px; letter-spacing: 0.8px;
    padding-top: 33px;
  }
</style>
</head>
<body>
  <main class="letterhead">
    <header>
      <div class="brand">
        <span class="brand-dot"></span>
        <div class="brand-name">Harbourline<br>Partners</div>
      </div>

      <div class="contact">
        <div class="practice">
          <p>Harbourline Partners Pty Ltd<br>is a QFA Practice</p>
          <span class="practice-badge" aria-label="QFA practice badge"></span>
        </div>
        <ul class="contact-list">
          <li>+61 3 9415 2286
            <svg viewBox="0 0 10 10" aria-hidden="true"><path d="M1 3 Q5 0 9 3 L8 5 L6 4 V3.5 H4 V4 L2 5 Z M2 6 H8 V9 H2 Z"/></svg>
          </li>
          <li>+61 3 9415 2287
            <svg viewBox="0 0 10 10" aria-hidden="true"><path d="M3 0 H7 V3 H3 Z M1 3.5 H9 V8 H1 Z M3 7 H7 V10 H3 Z"/></svg>
          </li>
          <li>www.harbourlinepartners.net.au
            <svg viewBox="0 0 10 10" aria-hidden="true"><circle cx="5" cy="5" r="4.5"/><path d="M0.5 5 H9.5 M5 0.5 V9.5" stroke="#fff" stroke-width="0.8"/></svg>
          </li>
          <li>hello@harbourlinepartners.net.au
            <svg viewBox="0 0 10 10" aria-hidden="true"><path d="M0 2 H10 V8 H0 Z"/><path d="M0 2 L5 6 L10 2" stroke="#fff" stroke-width="0.8" fill="none"/></svg>
          </li>
        </ul>
        <p class="address">Suite 412, 88 Ferncroft Lane<br>Ashvale Victoria 3190</p>
      </div>
    </header>

    <div class="footer-rule"></div>
    <footer class="footer">
      Liability limited by a scheme approved<br>under Professional Standards Legislation
    </footer>
  </main>
</body>
</html>
```